Banner Design for High End Jewelry Website

We need a banner for our website (brindlestone.com) for a sale that we will be running. The banner should be a size 1187 × 400. I have included a few pieces of jewelry to be included in the banner (do not need to use all, can use just some). The banner should say:
"Christmas is Closer Than You Think Sale!"
Shop Now

Industry/Entity Type

Jewelry

```html
<!DOCTYPE html>
<html lang="en">
<head>
<meta charset="utf-8">
<title>Brindlestone Christmas Sale Banner</title>
<link rel="stylesheet" href="https://fonts.googleapis.com/css2?family=Questrial&display=swap">
<style>
  :root {
    --page-bg: #ffffff;
    --panel-bg: #f2f2f2;
    --rule: #8e8e8e;
    --ink: #111111;
    --gold-light: #f0d36a;
    --gold-mid: #ddb53e;
    --gold-deep: #b8902a;
  }
  * { margin: 0; padding: 0; box-sizing: border-box; }
  html, body {
    width: 1200px;
    height: 404px;
    overflow: hidden;
    background: var(--page-bg);
  }
  .banner {
    position: relative;
    width: 1200px;
    height: 404px;
    font-family: "Questrial", "Century Gothic", sans-serif;
    color: var(--ink);
  }
  .banner__panel {
    position: absolute;
    left: 20px;
    top: 20px;
    width: 1146px;
    height: 358px;
    background: var(--panel-bg);
  }
  .banner__rule-top {
    position: absolute;
    left: 20px;
    top: 19px;
    width: 1146px;
    height: 4px;
    background: var(--rule);
  }
  .banner__rule-bottom {
    position: absolute;
    top: 375px;
    height: 4px;
    background: var(--rule);
  }
  .banner__rule-bottom--left { left: 20px; width: 443px; }
  .banner__rule-bottom--right { left: 725px; width: 441px; }
  .banner__product {
    position: absolute;
    left: 0;
    top: 0;
  }
  .banner__headline {
    position: absolute;
    left: 0;
    width: 1190px;
    top: 166px;
    text-align: center;
    font-size: 27px;
    letter-spacing: 2.6px;
    font-weight: 400;
    text-transform: uppercase;
    line-height: 1;
  }
  .banner__cta {
    position: absolute;
    left: 0;
    width: 1190px;
    top: 208px;
    text-align: center;
    font-size: 36px;
    letter-spacing: 2.5px;
    font-weight: 400;
    text-transform: uppercase;
    line-height: 1;
  }
  .banner__site {
    position: absolute;
    left: 463px;
    width: 262px;
    top: 369px;
    text-align: center;
    font-size: 12px;
    letter-spacing: 2.6px;
    text-transform: uppercase;
    line-height: 16px;
  }
</style>
</head>
<body>
  <div class="banner">
    <div class="banner__panel"></div>
    <div class="banner__rule-top"></div>

    <svg class="banner__product" width="1200" height="404" viewBox="0 0 1200 404"
         role="img" aria-label="Photograph of a gold scale-patterned cuff bracelet set with diamonds">
      <defs>
        <linearGradient id="gold" x1="0" y1="0" x2="1" y2="1">
          <stop offset="0" stop-color="var(--gold-light)"/>
          <stop offset="0.55" stop-color="var(--gold-mid)"/>
          <stop offset="1" stop-color="var(--gold-deep)"/>
        </linearGradient>
      </defs>
      <ellipse cx="596" cy="200" rx="112" ry="178" transform="rotate(36 596 200)" fill="url(#gold)"/>
    </svg>

    <h1 class="banner__headline">Christmas is closer thank you think sale !</h1>
    <p class="banner__cta">Shop now !!</p>

    <div class="banner__rule-bottom banner__rule-bottom--left"></div>
    <div class="banner__rule-bottom banner__rule-bottom--right"></div>
    <p class="banner__site">www.brindlestone.com</p>
  </div>
</body>
</html>
```